Halvorsen Partners Business Card

Halvorsen Partners Civil Construction
Marcus Halvorsen
CEO
727-518-6094
Marcus@HalvorsenSiteworks.example
www.HalvorsenSiteworks.example
Site Development
Utility Construction
Excavation
40876 County Lane 19
Pine Harbor, FL 34690

Target Market(s)

Construction and government

Industry/Entity Type

Business

Contact Information for Business Card

I want an unique design that make a statement

Number of Pages Required

1 page

Font styles to use

Colors

Designer to choose colors to be used in the design.

Requirements
Must have
• unique design, feel free to modify or change the color of my logo.
Nice to have
• extra design features like spot UV, foil accents, color edges, unique paper, or any thing that would make my card pop.
• I like the feel of the image that I attached

```html
<!DOCTYPE html>
<html lang="en">
<head>
<meta charset="UTF-8">
<title>Halvorsen Partners Business Card</title>
<link href="https://fonts.googleapis.com/css2?family=Catamaran:wght@400;600;700&display=swap" rel="stylesheet">
<style>
  :root {
    --navy: #1d3e62;
    --navy-deep: #133453;
    --navy-light: #24507a;
    --stone: #7d7f81;
    --silver: #a6a7a8;
    --paper: #efeeea;
    --paper-edge: #e4e3de;
    --stage: #1c1c1c;
    --white: #ffffff;
  }
  * { box-sizing: border-box; margin: 0; padding: 0; }
  html, body { width: 1200px; height: 1076px; overflow: hidden; }
  body {
    background: var(--stage);
    font-family: "Catamaran", "Helvetica Neue", Arial, sans-serif;
    position: relative;
  }
  .card {
    position: absolute;
    left: 190px;
    width: 820px;
    height: 473px;
    overflow: hidden;
    box-shadow: 0 10px 30px rgba(0,0,0,.55);
  }
  /* Back side */
  .card--back {
    top: 45px;
    border-radius: 16px 120px 16px 16px;
    background: var(--navy-deep);
  }
  .back-rays {
    position: absolute; inset: 0;
    background: radial-gradient(circle at 50% 50%, var(--navy-light) 0%, var(--navy-deep) 70%);
  }
  .back-brand {
    position: absolute; left: 0; right: 0; top: 50%;
    transform: translateY(-50%);
    display: flex; align-items: center; justify-content: center; gap: 22px;
    color: var(--white);
  }
  .brand-square {
    width: 70px; height: 70px; border: 8px solid currentColor; flex: none;
  }
  .brand-name {
    font-weight: 700; line-height: 1; text-transform: uppercase;
  }
  .brand-name .line-main { display: block; font-size: 44px; letter-spacing: .5px; }
  .brand-name .line-sub { display: block; font-size: 22px; letter-spacing: 6px; margin-top: 8px; }

  /* Front side */
  .card--front {
    top: 558px;
    border-radius: 120px 16px 16px 16px;
    background: linear-gradient(160deg, var(--paper) 0%, var(--paper-edge) 100%);
  }
  .front-brand {
    position: absolute; left: 44px; top: 76px;
    display: flex; align-items: center; gap: 18px;
    color: var(--navy);
  }
  .front-brand .brand-square { width: 92px; height: 92px; border-width: 10px; }
  .front-brand .divider { width: 2px; height: 110px; background: var(--silver); }
  .front-brand .line-main { font-size: 40px; }
  .front-brand .line-sub { font-size: 21px; letter-spacing: 5.5px; color: var(--stone); }

  .person { position: absolute; left: 46px; top: 222px; }
  .person-name { font-size: 29px; font-weight: 700; color: var(--navy); text-transform: uppercase; line-height: 1.1; }
  .person-role { font-size: 21px; color: var(--stone); line-height: 1.1; }

  .contact { position: absolute; left: 46px; top: 312px; list-style: none; }
  .contact li {
    display: flex; align-items: center; gap: 9px;
    font-size: 21px; color: var(--stone); height: 31px;
  }
  .contact .web { color: var(--navy); }
  .icon {
    width: 24px; height: 24px; background: var(--navy); border-radius: 3px;
    display: flex; align-items: center; justify-content: center; flex: none;
  }
  .address {
    position: absolute; right: 42px; top: 222px;
    text-align: right; font-size: 23px; color: var(--stone); line-height: 1.25;
  }
  .services {
    position: absolute; right: 42px; top: 312px; list-style: none; text-align: right;
  }
  .services li {
    font-size: 21px; color: var(--stone); height: 31px;
    display: flex; align-items: center; justify-content: flex-end; gap: 12px;
  }
  .services li::after {
    content: ""; width: 12px; height: 12px; border-radius: 50%; background: var(--navy);
  }
  .wave { position: absolute; left: 0; bottom: 0; width: 820px; height: 80px; }
</style>
</head>
<body>

  <section class="card card--back" aria-label="Card back">
    <div class="back-rays" role="img" aria-label="Navy sunburst ray pattern"></div>
    <div class="back-brand">
      <span class="brand-square"></span>
      <span class="brand-name">
        <span class="line-main">Halvorsen Partners</span>
        <span class="line-sub">Civil Construction</span>
      </span>
    </div>
  </section>

  <section class="card card--front" aria-label="Card front">
    <div class="front-brand">
      <span class="brand-square"></span>
      <span class="divider"></span>
      <span class="brand-name">
        <span class="line-main">Halvorsen Partners</span>
        <span class="line-sub">Civil Construction</span>
      </span>
    </div>

    <div class="person">
      <p class="person-name">Marcus Halvorsen</p>
      <p class="person-role">CEO</p>
    </div>

    <ul class="contact">
      <li>
        <span class="icon"><svg width="16" height="16" viewBox="0 0 16 16"><path d="M4 1.5l2.2 3-1.3 1.5c.8 1.8 2.2 3.2 4 4l1.5-1.3 3 2.2-1.2 2.6C7 13.3 2.7 9 1.4 2.7z" fill="#fff"/></svg></span>
        727-518-6094
      </li>
      <li>
        <span class="icon"><svg width="16" height="16" viewBox="0 0 16 16"><rect x="1.5" y="3.5" width="13" height="9" fill="none" stroke="#fff" stroke-width="1.4"/><path d="M1.5 3.5L8 9l6.5-5.5" fill="none" stroke="#fff" stroke-width="1.4"/></svg></span>
        Marcus@HalvorsenSiteworks.example
      </li>
      <li class="web">
        <span class="icon"><svg width="16" height="16" viewBox="0 0 16 16"><circle cx="8" cy="8" r="6" fill="none" stroke="#fff" stroke-width="1.4"/><ellipse cx="8" cy="8" rx="2.6" ry="6" fill="none" stroke="#fff" stroke-width="1.2"/><path d="M2 8h12" stroke="#fff" stroke-width="1.2"/></svg></span>
        www.HalvorsenSiteworks.example
      </li>
    </ul>

    <p class="address">40876 County Lane 19<br>Pine Harbor, FL 34690</p>

    <ul class="services">
      <li>Site Development</li>
      <li>Utility Construction</li>
      <li>Excavation</li>
    </ul>

    <svg class="wave" viewBox="0 0 820 80" preserveAspectRatio="none" aria-hidden="true">
      <path d="M0 8 C160 60 380 66 560 40 C680 22 760 12 820 10 L820 80 L0 80 Z" fill="#a6a7a8"/>
      <path d="M0 22 C170 72 390 74 570 50 C690 34 770 26 820 24 L820 80 L0 80 Z" fill="#efeeea"/>
      <path d="M0 30 C180 78 400 78 580 56 C700 42 775 34 820 32 L820 80 L0 80 Z" fill="#1d3e62"/>
    </svg>
  </section>

</body>
</html>
```